SIMPLE & POWERFUL Full Page Magazine Ad for Security Consultancy

The Task: Design a full page advertisement for placement in an industry trade show publication. Simple but powerful ad with a clean look.
The Company: Brackwater Advisory, LLC (www.brackwaterteam.us) will be placing a full page ad (details attached) in the annual trade show publication for the New York City Chapter of LORV Worldwide (www.lorvchapter.org). The worlds largest security association. We are a security consulting company that provides security consulting, security engineering, and security training services.
The Audience: Facility Security Directors, Retired Law Enforcement now in private security, and other security firms.
The Goal: The idea is to create an ad that truly stands out from the rest. Think outside the box. The Ad needs to speak volumes but say little. The lasting impression should be that we (Brackwater) are security solution providers, we fix security problems.
Example: A yellow banana peel and a foot in a dress shoe about to step on it with the wording; "Brackwater knows how slippery a security project can be, let us help you navigate your next security project"
or
Example: A puzzle making the word SECURITY and the wording; "Let Brackwater solve your next security puzzle"
Again, think outside the box. Simple and powerful.
Last Years Magazine: https://lorvchapter.org/media/LORV-Security-Director-2014.pdf

Target Market(s)
Security directors and facility directors of NYC buildings
Industry/Entity Type
Industry
Font styles to use
Requirements
Must have
- Ad Must Include:
- 1. Our Logo (attached)
- 2. Our Services (Security Consulting, Security Engineering, Managed Security Services, Security Training)
- 3. The slogan "We Know Security"
- 4. Our Address: Four Garrick Court, 22nd Floor, New York, NY 10027
- 5. Our Phone Number: 888-416-275
- 6. Our web address: www.brackwaterteam.us
- 7. Our email: info@brackwaterteam.us
Nice to have
- Images or artwork thats supports the idea of the Ad.

```html
<!DOCTYPE html>
<html lang="en">
<head>
<meta charset="utf-8">
<title>Brackwater Advisory – Full Page Ad</title>
<link rel="stylesheet" href="https://fonts.googleapis.com/css2?family=Carlito:ital,wght@0,400;0,700;1,400&display=swap">
<style>
  :root {
    --ink: #222222;
    --navy: #1b1f66;
    --night: #000000;
    --mist: #ffffff;
    --brand-grey: #3a3a3c;
    --apple-red: #b01a1f;
    --lemon: #d4c82a;
  }
  * { box-sizing: border-box; margin: 0; padding: 0; }
  html, body { width: 939px; height: 1200px; overflow: hidden; background: var(--mist); }
  body { font-family: "Carlito", "Calibri", sans-serif; color: var(--ink); }
  .ad { position: relative; width: 939px; height: 1200px; overflow: hidden; background: var(--mist); }
  .backdrop {
    position: absolute; left: 13px; top: 13px; width: 912px; height: 800px;
    background: linear-gradient(to bottom, var(--night) 0%, #0c0c0c 38%, #3c3c3c 55%, #8e8e8e 70%, #d8d8d8 84%, var(--mist) 100%);
  }
  .headline {
    position: absolute; top: 99px; left: 0; width: 100%; text-align: center;
    color: var(--mist); font-weight: 700; font-size: 34.5px;
  }
  .hero-photo {
    position: absolute; left: 283px; top: 229px; width: 390px; height: 410px;
    background: linear-gradient(to right, #8a1418 0%, var(--apple-red) 40%, var(--lemon) 60%, #b3a91c 100%);
  }
  .copy {
    position: absolute; top: 703px; width: 376px;
    font-size: 16.3px; line-height: 26px;
  }
  .copy--intro { left: 82px; text-align: justify; }
  .copy--services { left: 483px; text-align: justify; }
  .services { list-style: none; margin-top: 26px; }
  .services li { color: var(--navy); font-weight: 700; font-size: 19px; line-height: 26px; }
  .services li::before { content: "•"; margin-right: 6px; }
  .slogan {
    position: absolute; top: 948px; left: 0; width: 100%; text-align: center;
    color: var(--navy); font-style: italic; font-size: 34.5px;
  }
  .brand {
    position: absolute; left: 72px; top: 1066px;
    display: flex; align-items: center; gap: 14px;
    color: var(--brand-grey); font-weight: 700; font-size: 54px; line-height: 1;
  }
  .brand-dot { width: 22px; height: 22px; border-radius: 50%; background: var(--brand-grey); }
  .contact { position: absolute; left: 565px; top: 1045px; list-style: none; }
  .contact li {
    display: flex; align-items: center; gap: 9px;
    height: 23.5px; font-size: 13.5px; font-weight: 700; color: var(--ink);
  }
  .contact svg { width: 15px; height: 15px; flex: none; }
</style>
</head>
<body>
<main class="ad">
  <div class="backdrop"></div>
  <h1 class="headline">We understand how security projects can go sour.</h1>

  <div class="hero-photo" role="img" aria-label="Photograph of a fruit that is half a glossy red apple and half a yellow lemon"></div>

  <p class="copy copy--intro">Security consulting is more than understanding security technology, we understand the why behind the what. Brackwater Advisory is a full-service security consulting and design firm whose diverse experience in security operations, emergency services, and technical fluency in security technology allows us to thoroughly understand the why before implementing security mitigation strategies.</p>

  <div class="copy copy--services">
    <p>Our services encompass all aspects of security planning including:</p>
    <ul class="services">
      <li>Security Consulting</li>
      <li>Security Engineering</li>
      <li>Managed Security Services</li>
      <li>Security Training</li>
    </ul>
  </div>

  <p class="slogan">We Know Security.</p>

  <div class="brand"><span class="brand-dot"></span>Brackwater</div>

  <ul class="contact">
    <li>
      <svg viewBox="0 0 16 16" fill="none" stroke="#1b1f66" stroke-width="1.4"><path d="M2 8 8 2.5 14 8M4 7v7h8V7M7 14v-4h2v4"/></svg>
      Four Garrick Court, 22nd Floor, New York, NY 10027
    </li>
    <li>
      <svg viewBox="0 0 16 16" fill="#1b1f66"><path d="M1 5c2-3 12-3 14 0l-2 2-2.5-1V4.5h-5V6L3 7z"/><rect x="3" y="8" width="10" height="6" rx="1"/></svg>
      888-416-275
    </li>
    <li>
      <svg viewBox="0 0 16 16" fill="none" stroke="#1b1f66" stroke-width="1.4"><rect x="1.5" y="3.5" width="13" height="9"/><path d="M1.5 3.5 8 9l6.5-5.5"/></svg>
      info@brackwaterteam.us
    </li>
    <li>
      <svg viewBox="0 0 16 16" fill="none" stroke="#1b1f66" stroke-width="1.2"><circle cx="8" cy="8" r="6.5"/><ellipse cx="8" cy="8" rx="3" ry="6.5"/><path d="M1.5 8h13M2.5 4.8h11M2.5 11.2h11"/></svg>
      www.brackwaterteam.us
    </li>
  </ul>
</main>
</body>
</html>
```